Go Stride San Antonio Training Program

This is a 5X7 card that will advertise our running training program. We personal coach and group coach 100's of runners for everything from a 5K to ultra-maathons. We want this to be inviting, un-intimidating an very professional. I have attached files and two logos. I want the two logos on the flyer and any of the photos.

Target Market(s)

Target customer is ANYONE interested in running and be coached for races.

Industry/Entity Type

Training

Requirements
Must have
• The Go Stride Training Program is designed to help Runners of all levels of experience and ability train for the race event of their choice.

Your coach will build your plan based on the following information:

-Current fitness level
-Goal
-Your commitment to the training (time you can commit to running)
-Progress

Training Program Benefits:

-Training Tech Shirt
-Training group meet ups between 6am and 7am (depending on weather and distance) every Saturday morning.
-Interval/Speed session every Tuesday night betwen 6-7pm
-Customized training program that is adjusted for you as you improve
-15% discount at Go Stride Store (for in store purchases only)
Cost and Details:

The training program is year round so we start when YOU want to start.
Training Program cost – $40/month
Nice to have
• I attached a bunch of photos, they do not all need to be used. Use them how you wish. I plan on handing this out to thousands of people. I really want it to be dynamic and well designed.

```html
<!DOCTYPE html>
<html lang="en">
<head>
<meta charset="utf-8">
<title>Go Stride San Antonio Training Program</title>
<link href="https://fonts.googleapis.com/css2?family=Delius&family=Open+Sans:wght@400;600;700&display=swap" rel="stylesheet">
<style>
  :root {
    --ink: #1a1a1a;
    --brand-red: #e0282a;
    --accent-yellow: #f3e24a;
    --text-light: #ffffff;
    --shade: rgba(10, 10, 12, 0.58);
    --sky: #dce7ee;
    --foliage: #b7c29a;
    --road: #55575b;
    --road-dark: #3a3b3e;
    --runner-orange: rgba(232, 84, 34, 0.55);
  }
  * { box-sizing: border-box; margin: 0; padding: 0; }
  html, body { width: 857px; height: 1200px; overflow: hidden; background: #fff; }
  .card {
    position: relative;
    width: 857px;
    height: 1200px;
    overflow: hidden;
    font-family: "Open Sans", Arial, sans-serif;
    color: var(--text-light);
  }
  .hero-photo {
    position: absolute; inset: 0;
    background:
      radial-gradient(ellipse 170px 330px at 42% 36%, var(--runner-orange), transparent 75%),
      radial-gradient(ellipse 160px 120px at 6% 40%, rgba(222, 206, 70, 0.55), transparent 70%),
      linear-gradient(180deg, var(--sky) 0%, #c9d6dc 22%, var(--foliage) 36%, #8f918b 48%, var(--road) 70%, var(--road-dark) 100%);
  }
  .shade-panel {
    position: absolute; top: 0; right: 0; bottom: 0; left: 360px;
    background: var(--shade);
  }
  .intro {
    position: absolute; left: 24px; top: 30px; width: 320px;
    font-family: "Delius", "Comic Sans MS", cursive;
    font-size: 20px; line-height: 31px; color: var(--ink);
  }
  .intro .program-name {
    color: var(--brand-red); font-weight: 700; font-size: 32px;
    font-family: "Open Sans", Arial, sans-serif; letter-spacing: 0.5px;
  }
  .plan-box {
    position: absolute; left: 468px; top: 72px; width: 325px; height: 250px;
    border: 2px solid var(--text-light);
    padding: 14px 10px 0 10px;
  }
  .plan-box h2 {
    color: var(--accent-yellow); font-weight: 400; text-align: center;
    font-size: 26px; line-height: 30px; margin-bottom: 12px;
  }
  .plan-factors { list-style: none; font-size: 18px; line-height: 25px; }
  .plan-factors .initial { color: var(--accent-yellow); font-size: 22px; }
  .benefits-title {
    position: absolute; left: 454px; top: 382px;
    color: var(--accent-yellow); font-weight: 600; font-size: 24px;
  }
  .benefits { position: absolute; left: 408px; top: 440px; width: 430px; list-style: none; }
  .benefits li {
    position: absolute; left: 0; display: flex; gap: 14px;
    font-size: 18px; line-height: 27px; width: 430px;
  }
  .benefits svg { flex: none; width: 24px; height: 24px; margin-top: 2px; }
  .benefit-shirt { top: 6px; }
  .benefit-group { top: 64px; }
  .benefit-interval { top: 176px; }
  .benefit-custom { top: 264px; }
  .benefit-discount { top: 367px; }
  .details-box {
    position: absolute; left: 450px; top: 898px; width: 356px; height: 237px;
    border: 2px solid var(--text-light);
    text-align: center; padding-top: 14px;
  }
  .details-box .year-round { color: var(--accent-yellow); font-size: 23px; line-height: 28px; }
  .details-box .year-round strong { color: var(--text-light); font-weight: 400; }
  .details-box .cost-label { color: var(--accent-yellow); font-size: 22px; margin-top: 26px; }
  .details-box .cost { font-size: 31px; line-height: 40px; }
  .details-box .cost .currency { color: var(--brand-red); }
  .brand-name {
    position: absolute; left: 42px; top: 760px; width: 224px;
    text-align: center; font-weight: 700; font-size: 36px; line-height: 42px;
    color: var(--text-light);
  }
  .partner-name {
    position: absolute; left: 26px; top: 1010px; width: 240px;
    text-align: center; font-weight: 600; font-size: 18px; line-height: 24px;
    color: var(--text-light);
  }
</style>
</head>
<body>
<main class="card">
  <div class="hero-photo" role="img" aria-label="Photo of a runner in an orange shirt and race bib running on a sunny road lined with yellow flowers and traffic cones"></div>
  <div class="shade-panel"></div>

  <p class="intro">The <span class="program-name">GO STRIDE</span> Training Program is designed to help Runners of all levels of experience and ability train for the race event of their choice.</p>

  <section class="plan-box">
    <h2>Your coach will build your plan based on</h2>
    <ul class="plan-factors">
      <li><span class="initial">C</span>urrent fitness level</li>
      <li><span class="initial">G</span>oal</li>
      <li><span class="initial">Y</span>our commitment to the training (time you can commit to running)</li>
      <li><span class="initial">P</span>rogress</li>
    </ul>
  </section>

  <h2 class="benefits-title">Training Program Benefits</h2>
  <ul class="benefits">
    <li class="benefit-shirt"><svg viewBox="0 0 24 24" aria-hidden="true"><circle cx="12" cy="12" r="11" fill="#f3e24a"/><path d="M6 12h10M12 7l5 5-5 5" stroke="#222" stroke-width="2.4" fill="none" stroke-linecap="round" stroke-linejoin="round"/></svg><span>Training Tech Shirt</span></li>
    <li class="benefit-group"><svg viewBox="0 0 24 24" aria-hidden="true"><circle cx="12" cy="12" r="11" fill="#f3e24a"/><path d="M6 12h10M12 7l5 5-5 5" stroke="#222" stroke-width="2.4" fill="none" stroke-linecap="round" stroke-linejoin="round"/></svg><span>Training group meet ups between 6am and 7am (depending on weather and distance) every Saturday morning.</span></li>
    <li class="benefit-interval"><svg viewBox="0 0 24 24" aria-hidden="true"><circle cx="12" cy="12" r="11" fill="#f3e24a"/><path d="M6 12h10M12 7l5 5-5 5" stroke="#222" stroke-width="2.4" fill="none" stroke-linecap="round" stroke-linejoin="round"/></svg><span>Interval/Speed session every Tuesday night betwen 6-7pm</span></li>
    <li class="benefit-custom"><svg viewBox="0 0 24 24" aria-hidden="true"><circle cx="12" cy="12" r="11" fill="#f3e24a"/><path d="M6 12h10M12 7l5 5-5 5" stroke="#222" stroke-width="2.4" fill="none" stroke-linecap="round" stroke-linejoin="round"/></svg><span>Customized training program that is adjusted for you as you improve</span></li>
    <li class="benefit-discount"><svg viewBox="0 0 24 24" aria-hidden="true"><circle cx="12" cy="12" r="11" fill="#f3e24a"/><path d="M6 12h10M12 7l5 5-5 5" stroke="#222" stroke-width="2.4" fill="none" stroke-linecap="round" stroke-linejoin="round"/></svg><span>15% discount at Go Stride Store (for in store purchases only)</span></li>
  </ul>

  <p class="brand-name">GO STRIDE<br>SAN ANTONIO</p>
  <p class="partner-name">CIBOLO TRAIL<br>RUNNING COMPANY</p>

  <section class="details-box">
    <p class="year-round">The training program is year round so we start when <strong>YOU</strong> want to start.</p>
    <p class="cost-label">Training Program cost</p>
    <p class="cost">40<span class="currency">$</span>/month</p>
  </section>
</main>
</body>
</html>
```